Create a Magazine Ad for an asbestos law firm

we need an 8 X 13 ad to be on the back of a magazine cover. We have the text Attached and want a similar look and feel to our website : www.harborvale-claims.example. The ad should be targeted to white males 55 years or older who are conservative and worked in industry or industrial plants. The main offer is a free case review and trying to get them to call the telephone number.

Target Market(s)

White collar men who worked in industrial plants. Age 55 years or older.

Industry/Entity Type

Legal

Requirements
Must have
• Pictures of white middle class conservative man or man and woman
Nice to have
• look at www.harborvale-claims.example to an. idea of what we are looking for

```html
<!DOCTYPE html>
<html lang="en">
<head>
<meta charset="utf-8">
<title>Mesothelioma Compensation – Free Case Evaluation</title>
<link rel="stylesheet" href="https://fonts.googleapis.com/css2?family=Montserrat:wght@600;700;800;900&family=Open+Sans:wght@400;600;700&family=Oswald:wght@600;700&display=swap">
<style>
  :root{
    --navy:#1b2f4e;
    --blue:#1d5b8c;
    --blue-dark:#16476f;
    --sky:#dcedf7;
    --gold:#f2b51d;
    --note:#ffe08a;
    --ink:#24313f;
    --white:#ffffff;
  }
  *{box-sizing:border-box;margin:0;padding:0}
  html,body{width:793px;height:1200px;overflow:hidden;background:var(--white)}
  body{font-family:"Open Sans",Arial,sans-serif;color:var(--ink)}
  .ad{position:relative;width:793px;height:1200px;background:var(--white);overflow:hidden}

  .headline{text-align:center;padding-top:38px;color:var(--navy);font-family:"Montserrat",Arial,sans-serif}
  .headline .kicker{font-size:54px;font-weight:900;line-height:1;letter-spacing:1px}
  .headline .disease{font-size:58px;font-weight:900;line-height:1.08;letter-spacing:1px}
  .headline .sub{font-size:24px;font-weight:800;margin-top:6px;letter-spacing:.5px}

  .hero{position:absolute;left:0;top:210px;width:793px;height:414px;background:linear-gradient(180deg,var(--white) 0,var(--sky) 25%,var(--sky) 100%)}
  .hero-photo{position:absolute;left:80px;top:15px;width:633px;height:215px;
    background:linear-gradient(120deg,#cfd6dc 0%,#e9ecef 45%,#b9c2cb 70%,#f1f2f3 100%)}

  .info-boxes{position:absolute;left:80px;top:440px;width:633px;height:172px;display:flex}
  .info-box{flex:1;color:var(--white);padding:11px 16px;font-size:11.5px;line-height:1.32}
  .info-box.causes{background:var(--blue)}
  .info-box.help{background:var(--blue-dark)}
  .info-box p{color:var(--note);font-weight:600;margin-bottom:7px}
  .info-box ul{list-style:none}
  .info-box li{position:relative;padding-left:19px;margin-bottom:5px}
  .info-box li::before{content:"";position:absolute;left:0;top:3px;width:10px;height:10px;border-radius:50%;background:var(--white)}

  .trust{position:absolute;left:40px;top:626px;width:713px;text-align:center}
  .trust h2{font-family:"Montserrat",Arial,sans-serif;color:var(--navy);font-weight:800;font-size:19px;line-height:1.15;display:flex;align-items:center;justify-content:center;gap:12px}
  .trust h2 .amount{font-size:40px;font-weight:900}
  .trust p{font-size:11px;line-height:1.35;margin-top:5px;padding:0 30px}

  .settlements{position:absolute;left:0;top:738px;width:793px;height:258px;background:var(--sky)}
  .settlements h3{font-family:"Montserrat",Arial,sans-serif;color:var(--navy);font-size:19px;font-weight:800;text-align:center;padding-top:11px}
  .settlements .intro{font-size:10.5px;line-height:1.35;text-align:center;padding:5px 70px 0}
  .grid{display:grid;grid-template-columns:repeat(3,1fr);gap:14px 16px;padding:14px 60px 0}
  .case{display:flex;gap:10px;align-items:flex-start}
  .case .icon{flex:none;width:46px;height:46px;border-radius:6px;background:var(--blue);display:flex;align-items:center;justify-content:center}
  .case .figure{font-family:"Oswald","Montserrat",Arial,sans-serif;color:var(--navy);font-size:32px;font-weight:700;line-height:1;white-space:nowrap}
  .case .figure sup{font-size:16px;vertical-align:top;position:relative;top:1px}
  .case .desc{font-size:11.5px;line-height:1.2;margin-top:4px}

  .cta{position:absolute;left:60px;top:1012px;width:673px;display:flex;justify-content:space-between}
  .cta .eligible{flex:none}
  .cta .eligible h4{font-family:"Montserrat",Arial,sans-serif;color:var(--navy);font-weight:800;font-size:17px;line-height:1.2;white-space:nowrap}
  .cta .eligible p{font-size:12.5px;margin-top:6px;width:260px;line-height:1.3}
  .cta .call{flex:none}
  .cta .call .lead{font-family:"Montserrat",Arial,sans-serif;color:var(--navy);font-size:18px;font-weight:700;white-space:nowrap}
  .cta .call .lead strong{font-weight:900}
  .cta .call .number{font-family:"Montserrat",Arial,sans-serif;color:var(--navy);font-size:34px;font-weight:900;display:flex;align-items:center;gap:8px;margin-top:2px;white-space:nowrap}
  .cta .call .number small{font-size:20px}
  .cta .call .firm{font-size:10px;margin-top:4px;white-space:nowrap}
</style>
</head>
<body>
<div class="ad">
  <header class="headline">
    <div class="kicker">DIAGNOSED WITH</div>
    <div class="disease">MESOTHELIOMA</div>
    <div class="sub">YOU COULD BE OWED COMPENSATION</div>
  </header>

  <section class="hero">
    <div class="hero-photo" role="img" aria-label="Photo of an older man in a suit and a woman on the phone reviewing a case at a desk"></div>
  </section>

  <section class="info-boxes">
    <div class="info-box causes">
      <p>It's very likely you developed this disease through asbestos exposure. Mesothelioma patients are getting multi-million dollar settlements, decades later, from:</p>
      <ul>
        <li>Exposure to asbestos products</li>
        <li>Ex-employers</li>
        <li>Talcum baby powder companies</li>
      </ul>
    </div>
    <div class="info-box help">
      <p>We can help you find out if you qualify for a case in minutes.</p>
      <ul>
        <li>We'll analyze your situation at no cost</li>
        <li>Determine how much compensation you might be entitled to</li>
        <li>Show you the next steps to get what you're owed</li>
      </ul>
    </div>
  </section>

  <section class="trust">
    <h2><span class="amount">$30 BILLION</span><span>IS AVAILABLE IN TRUST FOR<br>MESOTHELIOMA PATIENTS</span></h2>
    <p>Tradesmen in many industries were negligently exposed to asbestos materials well into the 1980s. Whether you developed Mesothelioma due to asbestos exposure or you're the surviving family of a lost loved one you could be entitled to significant compensation.</p>
  </section>

  <section class="settlements">
    <h3>How much Money Can People Receive from a Mesothelioma Case?</h3>
    <p class="intro">Depending on where you were exposed and a few other factors, you can get a settlement from 6 to 7 figures. Here are a few examples of Mesothelioma Settlements received by our clients. These figures are the total compensation after all attorney fees and expenses are deducted.</p>
    <div class="grid">
      <div class="case">
        <div class="icon"><svg width="30" height="22" viewBox="0 0 30 22"><rect x="1" y="3" width="17" height="12" fill="#f2b51d"/><path d="M18 7h6l4 4v4H18z" fill="#f2b51d"/><circle cx="7" cy="17" r="3" fill="#fff"/><circle cx="23" cy="17" r="3" fill="#fff"/></svg></div>
        <div><div class="figure"><sup>$</sup>6,142,500</div><div class="desc">Exposed through<br>heavy duty vehicles</div></div>
      </div>
      <div class="case">
        <div class="icon"><svg width="30" height="22" viewBox="0 0 30 22"><rect x="11" y="2" width="8" height="7" fill="#fff"/><path d="M2 10h26l-4 8H6z" fill="#f2b51d"/><path d="M1 20q4-2 7 0t7 0 7 0 7 0" stroke="#fff" stroke-width="1.5" fill="none"/></svg></div>
        <div><div class="figure"><sup>$</sup>5,939,010</div><div class="desc">Exposed through<br>boat repair</div></div>
      </div>
      <div class="case">
        <div class="icon"><svg width="30" height="22" viewBox="0 0 30 22"><path d="M4 9l22-6v16L4 13z" fill="#f2b51d"/><rect x="13" y="1" width="3" height="7" fill="#fff"/></svg></div>
        <div><div class="figure"><sup>$</sup>3,600,450</div><div class="desc">Exposed through<br>navy service</div></div>
      </div>
      <div class="case">
        <div class="icon"><svg width="30" height="24" viewBox="0 0 30 24"><path d="M5 12a10 10 0 0 1 20 0z" fill="#f2b51d"/><rect x="3" y="12" width="24" height="4" fill="#fff"/></svg></div>
        <div><div class="figure"><sup>$</sup>6,033,510</div><div class="desc">Exposed through<br>general contracting</div></div>
      </div>
      <div class="case">
        <div class="icon"><svg width="30" height="22" viewBox="0 0 30 22"><path d="M2 11h26l-4 8H6z" fill="#f2b51d"/><rect x="10" y="4" width="10" height="6" fill="#fff"/></svg></div>
        <div><div class="figure"><sup>$</sup>3,921,750</div><div class="desc">Exposed through<br>navy service</div></div>
      </div>
      <div class="case">
        <div class="icon"><svg width="22" height="28" viewBox="0 0 22 28"><rect x="6" y="1" width="10" height="5" fill="#fff"/><rect x="3" y="6" width="16" height="20" rx="3" fill="#f2b51d"/></svg></div>
        <div><div class="figure"><sup>$</sup>2.5 MILLION</div><div class="desc">Exposed from<br>Talcum Baby Powder Maker</div></div>
      </div>
    </div>
  </section>

  <section class="cta">
    <div class="eligible">
      <h4>FIND OUT IF YOU'RE ELIGIBLE,<br>FOR FREE, IN MINUTES</h4>
      <p>We'll evaluate your situation and tell you what your case could be worth.</p>
    </div>
    <div class="call">
      <div class="lead">GET YOUR <strong>FREE EVALUATION</strong> NOW!</div>
      <div class="number"><small>CALL</small>
        <svg width="28" height="28" viewBox="0 0 24 24"><path d="M6.6 10.8a15 15 0 0 0 6.6 6.6l2.2-2.2a1 1 0 0 1 1-.25 11.4 11.4 0 0 0 3.6.57 1 1 0 0 1 1 1V20a1 1 0 0 1-1 1A17 17 0 0 1 3 4a1 1 0 0 1 1-1h3.5a1 1 0 0 1 1 1c0 1.25.2 2.45.57 3.57a1 1 0 0 1-.25 1z" fill="#1b2f4e"/></svg>
        12-555-0188</div>
      <div class="firm">Calloway &amp; Brandt, LLP, Martin Calloway, Austin, TX</div>
    </div>
  </section>
</div>
</body>
</html>
```